Website Design für Reinigungsunternehmen
Zielgruppe
Wir sind ein Reinigungsunternehmen, dass seit 2014 am Markt ist.
Was machen wir:
Das Angebot besteht darin, Räume nach dem IFSG (Infektionsschutzgesetz) und den Richtlinien des Werner Lasko Instituts mit ausgewählten Verfahren keimfrei zu bekommen.
Hygiene und prophylaktische Desinfektion sind für die Nutzung stark frequentierter Räume und Oberflächen gerade jetzt essentiell, denn die Ausbreitung von Viren und Bakterien kann auch durch präventive Maßnahmen eingedämmt werden.
Das Angebot ist, mit speziellen Reinigungsverfahren in Kombination mit Kaltverneblung ,die Räume fast vollständig von Keimen, Viren und Bakterien zu befreien.
So ist auch die Desinfektion von schwer zugänglichen Stellen und Gegenständen gewährleistet. Die eingesetzte Kaltnebeltechnologie wirkt in Verbindung mit Wasserstoffperoxid in verschiedenen Konzentrationen sowohl bakterizid, viruzid als auch fungizid. Wasserstoffperoxid wird rückstandsfrei abgebaut. Nach einer Einwirkzeit kann der behandelte, desinfizierte Raum sofort mechanisch gelüftet werden – ohne Material oder Umweltschäden zu riskieren.
Hier ein kurzes und erklärendes Video: https://klipvid.example/Qx7tmRwPaen
Aufgabenstellung
Die Website Soll maximal 3 Seiten haben.. Home (bzw. was wir machen..) Über uns (wer wir sind..) und Kontakt (-daten.
Ich möchte relativ kurz und knapp zum Thema kommen. Wenig Text, nur das wesentliche auf den Punkt gebracht - dafür ein ansprechendes professionelles Design. Bitte keine Bilder mit Gebäude, Reiniger etc. - dafür andere kreative Assoziationen einbringen.

```html
<!DOCTYPE html>
<html lang="de">
<head>
<meta charset="utf-8">
<title>aquor Gebäudereinigung</title>
<link href="https://fonts.googleapis.com/css2?family=Montserrat:wght@400;500;600;700;800&display=swap" rel="stylesheet">
<style>
:root{
  --navy:#1f3260;
  --sky:#6ba8d4;
  --white:#ffffff;
  --footer:#f0f0f0;
  --field:#dedede;
  --line:#d2d2d2;
  --water-a:#dbe9f4;
  --water-b:#9cc4e2;
}
*{margin:0;padding:0;box-sizing:border-box}
html,body{width:1072px;height:1200px;overflow:hidden}
body{font-family:'Montserrat',sans-serif;color:var(--navy);background:var(--white);position:relative}
.abs{position:absolute}

/* hero */
.hero{position:absolute;left:0;top:0;width:1072px;height:509px;background:var(--white);overflow:hidden}
.splash{position:absolute;border-radius:48% 52% 40% 60% / 30% 40% 60% 70%;background:linear-gradient(160deg,var(--water-a),var(--water-b) 60%,var(--water-a));opacity:.85}
.splash-left{left:150px;top:-10px;width:160px;height:487px;transform:rotate(-6deg)}
.splash-right{left:760px;top:88px;width:170px;height:440px;transform:rotate(5deg)}
.nav{position:absolute;top:22px;left:0;width:1072px;height:27px}
.nav a{position:absolute;top:0;height:27px;line-height:25px;font-size:10px;font-weight:600;color:var(--navy);text-decoration:none;letter-spacing:.2px}
.nav .active{left:393px;width:66px;border:1.5px solid var(--sky);border-radius:14px;text-align:center;color:var(--sky);font-weight:700}
.nav .services{left:490px}
.nav .contact{left:611px}
.brand{position:absolute;top:128px;left:0;width:1072px;display:flex;justify-content:center;align-items:center;gap:12px}
.brand-dot{width:42px;height:42px;border-radius:50%;background:var(--navy)}
.brand-name{font-size:48px;font-weight:600;color:var(--navy);line-height:1}
.headline{position:absolute;left:0;width:1072px;text-align:center;font-weight:800;line-height:1}
.headline-main{top:224px;font-size:56px;color:var(--navy);letter-spacing:-.5px}
.headline-sub{top:271px;font-size:34.5px;font-weight:700;color:var(--sky)}
.lead{position:absolute;top:334px;left:0;width:1072px;text-align:center;font-size:12.5px;font-weight:500;line-height:15px;color:var(--navy)}
.lead strong{color:var(--sky);font-weight:700}
.btn{position:absolute;left:486px;top:418px;width:100px;height:28px;border-radius:14px;background:var(--sky);color:var(--white);font-size:10px;font-weight:700;text-align:center;line-height:28px;box-shadow:0 3px 4px rgba(31,50,96,.25)}

/* services band */
.band{position:absolute;left:0;top:509px;width:1072px;height:525px;background:var(--navy)}
.card{position:absolute;top:98px;width:207px;height:206px;border-radius:24px;background:var(--sky);color:var(--white);box-shadow:0 4px 8px rgba(0,0,0,.2)}
.card.light{background:var(--white);color:var(--sky)}
.card-1{left:210px}.card-2{left:433px}.card-3{left:657px}
.card svg{position:absolute;left:24px;top:20px}
.card h3{position:absolute;left:24px;top:70px;width:170px;font-size:15.5px;font-weight:700;line-height:14px}
.card p{position:absolute;left:25px;font-size:8.5px;line-height:9.5px;font-weight:400}
.card-1 p{top:120px}.card-2 p,.card-3 p{top:118px}
.card .more{position:absolute;left:25px;top:167px;font-size:10px;font-weight:700;display:flex;align-items:center;gap:9px}
.cta{position:absolute;top:360px;left:0;width:1072px;text-align:center;line-height:20px}
.cta .white{font-size:21px;font-weight:700;color:var(--white)}
.cta .blue{font-size:25px;font-weight:700;color:var(--sky);line-height:22px}
.phone-pill{position:absolute;left:451px;top:445px;width:187px;height:27px;background:var(--white);border-radius:14px;font-size:16.5px;font-weight:700;color:var(--navy);line-height:27px;padding-left:20px}
.phone-circle{position:absolute;left:433px;top:440px;width:36px;height:36px;border-radius:50%;background:var(--sky);display:flex;align-items:center;justify-content:center}

/* footer */
.footer{position:absolute;left:0;top:1034px;width:1072px;height:166px;background:var(--footer);font-size:8.5px;color:var(--navy)}
.footer-brand{position:absolute;left:210px;top:28px;display:flex;align-items:center;gap:5px}
.footer-brand .dot{width:17px;height:17px;border-radius:50%;background:var(--navy)}
.footer-brand .name{font-size:20px;font-weight:600;line-height:1}
.address{position:absolute;left:210px;top:66px;line-height:9.5px}
.address b{color:var(--sky);font-weight:700}
.col-title{position:absolute;top:35px;font-size:8px;font-weight:700;letter-spacing:.2px}
.links{position:absolute;left:433px;top:64px;line-height:18.7px}
.contacts{position:absolute;left:544px;top:64px;line-height:18.7px}
.contacts div{display:flex;align-items:center;gap:5px}
.field{position:absolute;left:711px;top:48px;width:152px;height:29px;background:var(--field);border-radius:5px;font-style:italic;color:#9a9a9a;font-size:8.5px;line-height:29px;padding-left:10px}
.field svg{position:absolute;right:8px;top:10px}
.note{position:absolute;left:711px;top:86px;width:150px;font-size:7px;line-height:7.5px}
.rule{position:absolute;left:210px;top:141px;width:653px;height:1px;background:var(--line)}
.rights{position:absolute;top:151px;left:0;width:1072px;text-align:center;font-size:7px;font-weight:500}
.rights b{color:var(--sky)}
</style>
</head>
<body>

<section class="hero">
  <div class="splash splash-left" role="img" aria-label="Wasserspritzer, hellblau und transparent"></div>
  <div class="splash splash-right" role="img" aria-label="Wasserspritzer mit Tropfen, hellblau und transparent"></div>

  <nav class="nav">
    <a class="active" href="#">HOME</a>
    <a class="services" href="#">LEISTUNGEN</a>
    <a class="contact" href="#">KONTAKT</a>
  </nav>

  <div class="brand"><span class="brand-dot"></span><span class="brand-name">aquor</span></div>

  <h1 class="headline headline-main">INNOVATIVE</h1>
  <h2 class="headline headline-sub">HYGIENEKONZEPTE</h2>

  <p class="lead">Wir schließen Reinigungslücken und befreien<br>Ihre Räumlichkeiten zu <strong>99,9 %</strong> von<br><strong>Viren, Bakterien und Keimen</strong></p>

  <div class="btn">LERN MEHR</div>
</section>

<section class="band">
  <article class="card card-1">
    <svg width="36" height="36" viewBox="0 0 36 36" fill="none" stroke="#fff" stroke-width="2"><path d="M6 12A14 14 0 0 1 30 10"/><path d="M30 24A14 14 0 0 1 6 26"/><path d="M26 6l4 4-5 2" fill="none"/><path d="M10 30l-4-4 5-2"/><path d="M18 10c3 5 5 7 5 10a5 5 0 0 1-10 0c0-3 2-5 5-10z" fill="#fff" stroke="none"/></svg>
    <h3>Flächen- und Raumdesinfektion gem. IFSG § 17</h3>
    <p>Lorem ipsum dolor sit amet,<br>consectetur adipiscing elit</p>
    <div class="more">LERN MEHR <svg width="14" height="10" viewBox="0 0 14 10" fill="none" stroke="#fff" stroke-width="2"><path d="M1 5h11M8 1l4 4-4 4"/></svg></div>
  </article>
  <article class="card card-2 light">
    <svg width="36" height="36" viewBox="0 0 36 36" fill="none" stroke="#6ba8d4" stroke-width="2"><path d="M6 12A14 14 0 0 1 30 10"/><path d="M30 24A14 14 0 0 1 6 26"/><path d="M26 6l4 4-5 2"/><path d="M10 30l-4-4 5-2"/><path d="M18 10c3 5 5 7 5 10a5 5 0 0 1-10 0c0-3 2-5 5-10z" fill="#6ba8d4" stroke="none"/></svg>
    <h3>WLI gelistete und geprüfte Verfahren</h3>
    <p>Lorem ipsum dolor sit amet,<br>consectetur adipiscing elit</p>
    <div class="more">LERN MEHR <svg width="14" height="10" viewBox="0 0 14 10" fill="none" stroke="#6ba8d4" stroke-width="2"><path d="M1 5h11M8 1l4 4-4 4"/></svg></div>
  </article>
  <article class="card card-3">
    <svg width="36" height="36" viewBox="0 0 36 36" fill="none" stroke="#fff" stroke-width="2"><path d="M6 12A14 14 0 0 1 30 10"/><path d="M30 24A14 14 0 0 1 6 26"/><path d="M26 6l4 4-5 2"/><path d="M10 30l-4-4 5-2"/><path d="M18 10c3 5 5 7 5 10a5 5 0 0 1-10 0c0-3 2-5 5-10z" fill="#fff" stroke="none"/></svg>
    <h3>Staatlich geprüfte Desinfektoren</h3>
    <p>Lorem ipsum dolor sit amet,<br>consectetur adipiscing elit</p>
    <div class="more">LERN MEHR <svg width="14" height="10" viewBox="0 0 14 10" fill="none" stroke="#fff" stroke-width="2"><path d="M1 5h11M8 1l4 4-4 4"/></svg></div>
  </article>

  <div class="cta">
    <div class="white">Vereinbaren Sie heute<br>noch einen Termin</div>
    <div class="blue">Rufen Sie uns an</div>
  </div>
  <div class="phone-pill">09471 / 512 304 70</div>
  <div class="phone-circle"><svg width="18" height="18" viewBox="0 0 24 24"><path fill="#fff" d="M6.6 10.8a15 15 0 0 0 6.6 6.6l2.2-2.2c.3-.3.7-.4 1-.2 1.1.4 2.3.6 3.6.6.6 0 1 .4 1 1V20c0 .6-.4 1-1 1A17 17 0 0 1 3 4c0-.6.4-1 1-1h3.5c.6 0 1 .4 1 1 0 1.3.2 2.5.6 3.6.1.3 0 .7-.2 1z"/></svg></div>
</section>

<footer class="footer">
  <div class="footer-brand"><span class="dot"></span><span class="name">aquor</span></div>
  <div class="address"><b>AQUOR GROUP</b><br>Gebäudereinigung &amp; Hygienekonzepte<br>Lindenweg 4<br>93099 Hollbach</div>

  <div class="col-title" style="left:433px">QUICK LINKS</div>
  <div class="links">HOME<br>LEISTUNGEN<br>KONTAKT</div>

  <div class="col-title" style="left:544px">KONTAKT UNS</div>
  <div class="contacts">
    <div><svg width="10" height="10" viewBox="0 0 24 24"><path fill="#6ba8d4" d="M6.6 10.8a15 15 0 0 0 6.6 6.6l2.2-2.2c.3-.3.7-.4 1-.2 1.1.4 2.3.6 3.6.6.6 0 1 .4 1 1V20c0 .6-.4 1-1 1A17 17 0 0 1 3 4c0-.6.4-1 1-1h3.5c.6 0 1 .4 1 1 0 1.3.2 2.5.6 3.6.1.3 0 .7-.2 1z"/></svg>09471 / 512 304 70</div>
    <div><svg width="10" height="10" viewBox="0 0 10 10"><rect x="2.5" y="0.5" width="5" height="3" fill="#6ba8d4"/><rect x="1" y="4" width="8" height="5" rx="1" fill="#6ba8d4"/></svg>09471 / 512 304 79</div>
    <div><svg width="10" height="8" viewBox="0 0 10 8"><rect width="10" height="8" rx="1" fill="#6ba8d4"/><path d="M0.5 1l4.5 3.5L9.5 1" stroke="#fff" fill="none"/></svg>mail@aquor-gruppe.de</div>
  </div>

  <div class="col-title" style="left:711px">NEWSLETTER</div>
  <div class="field">Email address<svg width="10" height="8" viewBox="0 0 10 8"><rect width="10" height="8" rx="1" fill="#6ba8d4"/><path d="M0.5 1l4.5 3.5L9.5 1" stroke="#fff" fill="none"/></svg></div>
  <div class="note">Lorem ipsum dolor sit amet, consectetur adipiscing elit</div>

  <div class="rule"></div>
  <div class="rights">ALL RIGHTS RESERVED BY <b>9FENNEL</b></div>
</footer>

</body>
</html>
```